Bright Path Attorneys Billboard Design for Personal Injury Law Firm

Need a billboard design that we can use for different versions. 1400px X 400px jpeg or png
I have attached the logo and the attorney for the billboard. Attorney Marla Benning
Here is a link to our current website brightpathlegalgroup.example

HEADLINE: HIT BY A TRUCK?
SUBHEAD: NO FEE. BIG FIGHT.
877-GRANTLY

HEADLINE: ACCIDENT?
SUBHEAD: NO FEE, UNLESS WE WIN!
877-GRANTLY

HEADLINE: BIG TRUCK. BIG CASE.
SUBHEAD: YOU PAY $0 UPFRONT
877-GRANTLY

Target Market(s)

People in Car Accident

Industry/Entity Type

Personal Injury Attorneys

```html
<!DOCTYPE html>
<html lang="en">
<head>
<meta charset="utf-8">
<title>Bright Path Attorneys – Billboard</title>
<link rel="stylesheet" href="https://fonts.googleapis.com/css2?family=Anton&display=swap">
<style>
  :root {
    --stage: #88898b;
    --board: #0e1013;
    --white: #ffffff;
    --gold: #f2b90f;
    --rule-fade: rgba(242, 185, 15, 0);
    --photo-dark: #0b0c0e;
    --photo-mid: #2a2d31;
    --photo-light: #5a5f66;
  }
  * { margin: 0; padding: 0; box-sizing: border-box; }
  html, body {
    width: 1200px;
    height: 439px;
    overflow: hidden;
    background: var(--stage);
  }
  .billboard {
    position: absolute;
    left: 60px;
    top: 69px;
    width: 1071px;
    height: 306px;
    background: var(--board);
    border: 1px solid #3a3c40;
    overflow: hidden;
    font-family: "Anton", "Impact", sans-serif;
  }
  .truck-photo {
    position: absolute;
    right: 0;
    top: 0;
    width: 330px;
    height: 100%;
    background:
      radial-gradient(ellipse at 70% 45%, var(--photo-light) 0%, var(--photo-mid) 35%, transparent 75%),
      linear-gradient(90deg, var(--board) 0%, var(--photo-dark) 25%, var(--photo-mid) 100%);
  }
  .message {
    position: absolute;
    left: 55px;
    top: 0;
    width: 628px;
    height: 100%;
    text-align: center;
    color: var(--white);
    text-transform: uppercase;
  }
  .headline {
    position: absolute;
    left: 0;
    right: 0;
    top: 8px;
    font-size: 94px;
    line-height: 1;
    letter-spacing: 0.5px;
  }
  .rule {
    position: absolute;
    left: 0;
    width: 100%;
    height: 3px;
    background: linear-gradient(90deg, var(--rule-fade) 0%, var(--gold) 12%, var(--gold) 88%, var(--rule-fade) 100%);
    border-radius: 2px;
  }
  .rule--top { top: 116px; }
  .rule--bottom { top: 213px; }
  .subhead {
    position: absolute;
    left: 0;
    right: 0;
    top: 133px;
    font-size: 70px;
    line-height: 1;
    color: var(--gold);
  }
  .phone {
    position: absolute;
    left: 0;
    right: 0;
    top: 224px;
    font-size: 56px;
    line-height: 1;
  }
  .firm-name {
    position: absolute;
    left: 770px;
    top: 232px;
    display: flex;
    align-items: center;
    gap: 12px;
    color: var(--white);
    text-transform: uppercase;
  }
  .firm-name__mark {
    width: 40px;
    height: 40px;
    background: var(--gold);
    flex: none;
  }
  .firm-name__text {
    font-size: 24px;
    line-height: 1.1;
    letter-spacing: 1px;
  }
</style>
</head>
<body>
  <div class="billboard">
    <div class="truck-photo" role="img" aria-label="Photo of a dark semi-truck front with grille and lit headlight"></div>

    <div class="message">
      <h1 class="headline">Hit by a truck?</h1>
      <div class="rule rule--top"></div>
      <p class="subhead">No fee. Big fight.</p>
      <div class="rule rule--bottom"></div>
      <p class="phone">877-GRANTLY</p>
    </div>

    <div class="firm-name">
      <span class="firm-name__mark"></span>
      <span class="firm-name__text">Bright Path<br>Attorneys</span>
    </div>
  </div>
</body>
</html>
```